Marlowe Hairdressing Business Card Design

The design has to be based upon a colour scheme of a black gloss background and silver type face letters and has to portray an exclusive and expensive outlet.

The business card has a dual use with the rear of the card being used for future appointments therefore this area has to be lined out to accept written text.

We also need to incorporate a Chatterbook log somewhere on the card.

Target Market(s)

High Earning individuals with high disposable incomes possible link too young professionals.

Contact Information for Business Card

Marlowe Hairdressing & The Willowmere Beauty
Tel 01632 418550
www.marlowehairdressing.example.co.uk

Requirements
Must have
• Company Name including beauty element, telephone number, website and chatterbook please.
Nice to have
• High Gloss finish with silver raised letters or similar
Should not have
• Hairdressing Images like, scissors, haircuts, beauty treatments etc

```html
<!DOCTYPE html>
<html lang="en">
<head>
<meta charset="utf-8">
<title>Marlowe Hairdressing – Business Card</title>
<link href="https://fonts.googleapis.com/css2?family=Michroma&family=Jura:wght@600&family=Open+Sans&display=swap" rel="stylesheet">
<style>
  :root {
    --canvas: #ffffff;
    --card-edge: #454346;
    --card-glow: #5f5f61;
    --silver-light: #f4f4f4;
    --silver-mid: #cfcfd0;
    --silver-dark: #a9a9ab;
    --ink: #111111;
    --type-silver: #e6e6e6;
  }
  * { margin: 0; padding: 0; box-sizing: border-box; }
  html, body { width: 1200px; height: 1000px; overflow: hidden; background: var(--canvas); }
  .canvas { position: relative; width: 1200px; height: 1000px; }

  .card {
    position: absolute;
    width: 575px; height: 379px;
    background: radial-gradient(ellipse 60% 60% at 50% 45%, var(--card-glow), var(--card-edge));
    overflow: hidden;
  }
  .card--front { left: 312px; top: 78px; }
  .card--back { left: 313px; top: 542px; }

  .card__decor {
    position: absolute; left: 0; top: 0;
    width: 260px; height: 379px;
    background:
      radial-gradient(ellipse 70% 45% at 30% 78%, rgba(190,190,192,0.35), rgba(190,190,192,0) 70%),
      radial-gradient(ellipse 60% 35% at 25% 20%, rgba(30,30,32,0.35), rgba(30,30,32,0) 70%);
  }

  .brand {
    position: absolute; right: 52px; top: 54px;
    text-align: right;
    font-family: "Michroma", sans-serif;
    font-weight: 400;
    font-size: 13px; line-height: 26px;
    letter-spacing: 1.2px;
    color: var(--type-silver);
    text-transform: uppercase;
  }
  .brand__line { display: block; }
  .brand__line .cap { font-size: 16px; }

  .contact {
    position: absolute; right: 42px;
    text-align: right;
    font-family: "Jura", sans-serif; font-weight: 600; font-style: normal;
    color: #ffffff; font-size: 13px; letter-spacing: 0.2px;
  }
  .contact--address { top: 229px; line-height: 19px; }
  .contact--lines { top: 281px; line-height: 19px; font-size: 12.5px; }
  .contact__row { display: flex; justify-content: flex-end; align-items: center; gap: 5px; }
  .contact__icon { width: 11px; height: 11px; flex: none; }
  .contact__square { width: 9px; height: 9px; background: #ffffff; margin: 0 1px; flex: none; }

  .pill {
    position: absolute;
    height: 31px;
    border-radius: 15px;
    border: 2px solid #8e8e90;
    background: linear-gradient(90deg, var(--silver-dark) 0%, var(--silver-mid) 12%, var(--silver-light) 40%, var(--silver-mid) 75%, var(--silver-dark) 100%);
    font-family: "Open Sans", sans-serif; font-size: 16px; color: var(--ink);
    display: flex; align-items: center; padding-left: 14px;
  }
  .pill__time { position: absolute; left: 250px; }
  .pill--heading { left: 43px; top: 42px; width: 240px; }
  .pill--field { left: 46px; width: 431px; }
</style>
</head>
<body>
<div class="canvas">

  <section class="card card--front">
    <div class="card__decor" role="img" aria-label="Decorative silver arc graphics"></div>

    <h1 class="brand">
      <span class="brand__line"><span class="cap">M</span>arlowe <span class="cap">H</span>airdressing</span>
      <span class="brand__line"><span class="cap">&amp;</span> <span class="cap">T</span>he <span class="cap">W</span>illowmere <span class="cap">B</span>eauty</span>
    </h1>

    <address class="contact contact--address">
      <div>17 Linden Row</div>
      <div>Ashcombe Fernley AB4 2QX</div>
    </address>

    <div class="contact contact--lines">
      <div class="contact__row">01632 418550
        <svg class="contact__icon" viewBox="0 0 12 12"><path d="M3 1 L5 3.5 L4 5 Q5.5 7.5 7.5 8.5 L9 7.5 L11 9.5 L9.5 11 Q4 10 1.5 3 Z" fill="#fff"/></svg>
      </div>
      <div class="contact__row">www.marlowehairdressing.example.co.uk
        <svg class="contact__icon" viewBox="0 0 12 12" fill="none" stroke="#fff" stroke-width="1"><circle cx="6" cy="6" r="5"/><ellipse cx="6" cy="6" rx="2.2" ry="5"/><path d="M1 6 H11 M2 3.5 H10 M2 8.5 H10"/></svg>
      </div>
      <div class="contact__row">info@marlowehairdressing.example.com
        <span class="contact__square"></span>
      </div>
    </div>
  </section>

  <section class="card card--back">
    <div class="pill pill--heading">Your Next Appointment</div>

    <div class="pill pill--field" style="top:84px">Stylist/Therapist</div>
    <div class="pill pill--field" style="top:127px;padding-left:18px">Date<span class="pill__time">Time</span></div>

    <div class="pill pill--field" style="top:173px">Stylist/Therapist</div>
    <div class="pill pill--field" style="top:216px;padding-left:18px">Date<span class="pill__time">Time</span></div>

    <div class="pill pill--field" style="top:262px">Stylist/Therapist</div>
    <div class="pill pill--field" style="top:305px;padding-left:18px">Date<span class="pill__time">Time</span></div>
  </section>

</div>
</body>
</html>
```